Business Card Design

I would like a new business card for my business Drive Haven, we operate within the automotive industry and offer customer retention solutions for independent mechanical workshops across Australia and New Zealand. The program incorporates service reminders and roadside assistance for consumers and is designed to get the client back for their vehicle service visit, I would like a doubled sided design that incorporates my logos and a two tone type card that has white and a carbon fibre look also use the blue in the logo I have uploaded. It would be great to have icons as the phone/fax/email etc details for the card are below. The finished design must be a print ready file useable.It would be great if the design could communicate the what type of business we are
Marcus Trelby
General Manager
Drive Haven Pty Ltd
Unit 5/42 Corrin Street
Wexmoor Newcastle NSW 2391
Ph:+61240173500
fax:+61240173600
Mobile:0415889214
Email:info@drivehaven-example.com.au
Updates
I have just upload a carbon fibre background for the business card hope it helps
Hello guys I am sorry fr no feedback I have been away over seas I will send feedback when I return monday
Industry/Entity Type
Automotive
Look and feel

```html
<!DOCTYPE html>
<html lang="en">
<head>
<meta charset="utf-8">
<title>Drive Haven – Business Card</title>
<link href="https://fonts.googleapis.com/css2?family=Dosis:wght@400;500;600&display=swap" rel="stylesheet">
<style>
  :root {
    --page-bg: #e9e7e4;
    --card-white: #f4f4f3;
    --card-white-glow: #ffffff;
    --carbon-dark: #0a2230;
    --carbon-mid: #0f3d52;
    --brand-blue: #1b9ad8;
    --ink-dark: #1c2227;
    --ink-light: #ffffff;
  }
  * { box-sizing: border-box; margin: 0; padding: 0; }
  html, body {
    width: 1200px; height: 1200px; overflow: hidden;
    background: var(--page-bg);
    font-family: "Dosis", "Arial Narrow", sans-serif;
  }
  .sheet {
    width: 1200px; height: 1200px;
    display: flex; flex-direction: column; align-items: center; justify-content: center;
    gap: 60px;
  }
  .card {
    width: 840px; height: 480px;
    border-radius: 28px;
    position: relative; overflow: hidden;
    box-shadow: 0 6px 22px rgba(0,0,0,0.18);
  }
  /* Front */
  .card-front {
    background: radial-gradient(circle at 50% 45%, var(--card-white-glow) 0%, var(--card-white) 55%, #e4e4e3 100%);
    display: flex; align-items: center; justify-content: center;
  }
  .brand {
    display: flex; align-items: center; gap: 26px;
  }
  .brand-dot {
    width: 96px; height: 96px; border-radius: 50%;
    background: var(--brand-blue);
  }
  .brand-name {
    font-size: 78px; font-weight: 500; letter-spacing: 3px;
    color: var(--ink-dark);
  }
  /* Back */
  .card-back {
    background:
      radial-gradient(ellipse at 60% 30%, var(--carbon-mid) 0%, var(--carbon-dark) 75%);
  }
  .back-circle {
    position: absolute; left: 430px; top: 40px;
    width: 240px; height: 240px; border-radius: 50%;
    background: var(--brand-blue); opacity: 0.22;
  }
  .contact {
    position: absolute; left: 56px; bottom: 44px;
    color: var(--ink-light);
  }
  .person-name { font-size: 42px; font-weight: 500; letter-spacing: 1px; line-height: 1.1; }
  .person-role { font-size: 24px; font-weight: 400; line-height: 1.2; }
  .company { font-size: 28px; font-weight: 400; line-height: 1.3; margin-bottom: 8px; }
  .row { display: flex; align-items: center; gap: 36px; font-size: 21px; line-height: 1.55; }
  .item { display: flex; align-items: center; gap: 8px; }
  .icon { width: 20px; height: 20px; fill: var(--brand-blue); flex: none; }
</style>
</head>
<body>
<main class="sheet">
  <section class="card card-front" aria-label="Card front">
    <div class="brand">
      <span class="brand-dot"></span>
      <span class="brand-name">Drive Haven</span>
    </div>
  </section>

  <section class="card card-back" role="img" aria-label="Card back on carbon fibre texture in deep blue">
    <span class="back-circle"></span>
    <div class="contact">
      <p class="person-name">Marcus Trelby</p>
      <p class="person-role">General Manager</p>
      <p class="company">Drive Haven Pty Ltd</p>
      <div class="row">
        <span class="item">
          <svg class="icon" viewBox="0 0 24 24"><path d="M6.6 10.8a15.1 15.1 0 0 0 6.6 6.6l2.2-2.2c.3-.3.7-.4 1-.2 1.1.4 2.3.6 3.6.6.6 0 1 .4 1 1V20c0 .6-.4 1-1 1A17 17 0 0 1 3 4c0-.6.4-1 1-1h3.5c.6 0 1 .4 1 1 0 1.3.2 2.5.6 3.6.1.3 0 .7-.2 1z"/></svg>
          Ph:+61240173500
        </span>
        <span class="item">
          <svg class="icon" viewBox="0 0 24 24"><path d="M7 3h10v5H7zM4 9h16a2 2 0 0 1 2 2v6h-4v4H6v-4H2v-6a2 2 0 0 1 2-2zm4 7v3h8v-3z"/></svg>
          fax:+61240173600
        </span>
        <span class="item">
          <svg class="icon" viewBox="0 0 24 24"><path d="M7 2h10a2 2 0 0 1 2 2v16a2 2 0 0 1-2 2H7a2 2 0 0 1-2-2V4a2 2 0 0 1 2-2zm0 3v13h10V5zm5 14.2a1 1 0 1 0 0 .1z"/></svg>
          Mobile:0415889214
        </span>
      </div>
      <div class="row">
        <span class="item">
          <svg class="icon" viewBox="0 0 24 24"><path d="M12 2a7 7 0 0 1 7 7c0 5-7 13-7 13S5 14 5 9a7 7 0 0 1 7-7zm0 4.5a2.5 2.5 0 1 0 0 5 2.5 2.5 0 0 0 0-5z"/></svg>
          Unit 5/42 Corrin Street, Wexmoor Newcastle NSW 2391
        </span>
      </div>
      <div class="row">
        <span class="item">
          <svg class="icon" viewBox="0 0 24 24"><path d="M3 5h18a1 1 0 0 1 1 1v12a1 1 0 0 1-1 1H3a1 1 0 0 1-1-1V6a1 1 0 0 1 1-1zm1 2.3V17h16V7.3l-8 5.5z"/></svg>
          Email:info@drivehaven-example.com.au
        </span>
      </div>
    </div>
  </section>
</main>
</body>
</html>
```